I need a business card design for a Boutique Pilates studio.

I would like to see designs similar to the one that I have uploaded.
thinking between two slogans:
'No ordinary place'
'Not so ordinary'

Contact Information for Business Card

Keva Pilates

```html
<!DOCTYPE html>
<html lang="en">
<head>
<meta charset="utf-8">
<title>Keva Pilates – Business Card</title>
<link href="https://fonts.googleapis.com/css2?family=Oswald:wght@400;600&family=Roboto:wght@400&display=swap" rel="stylesheet">
<style>
  :root {
    --backdrop: #3d3d3d;
    --card-dark: #2e2e2e;
    --card-yellow: #f7dc00;
    --accent: #f7dc00;
    --ink-light: #ffffff;
    --ink-dark: #111111;
    --divider: #6a6a6a;
  }
  * { margin: 0; padding: 0; box-sizing: border-box; }
  html, body {
    width: 1200px; height: 803px; overflow: hidden;
    background: var(--backdrop);
  }
  .stage {
    width: 1200px; height: 803px;
    display: flex; align-items: center; justify-content: center; gap: 40px;
  }
  .card {
    width: 520px; height: 297px;
    border-radius: 22px;
    position: relative;
  }
  .card--back { background: var(--card-dark); color: var(--ink-light); }
  .card--front { background: var(--card-yellow); color: var(--ink-dark); }

  /* Back side */
  .contact {
    position: absolute; left: 0; right: 0; top: 92px;
    display: flex; justify-content: center; align-items: stretch;
  }
  .person {
    text-align: right; padding-right: 16px;
    font-family: "Roboto", Arial, sans-serif; font-size: 13px; line-height: 1.3;
  }
  .person__name {
    font-family: "Oswald", "Arial Narrow", sans-serif; font-weight: 600;
    color: var(--accent); font-size: 22px; line-height: 1.1; letter-spacing: .3px;
  }
  .person__role { font-size: 13px; margin-bottom: 10px; }
  .divider { width: 1px; background: var(--divider); }
  .details {
    list-style: none; padding-left: 14px;
    font-family: "Roboto", Arial, sans-serif; font-size: 13px; line-height: 1.45;
  }
  .details li { display: flex; align-items: center; gap: 8px; }
  .details svg { width: 11px; height: 11px; flex: none; }
  .slogan {
    position: absolute; left: 0; right: 0; bottom: 56px; text-align: center;
    font-family: "Roboto", Arial, sans-serif; font-size: 13px;
  }

  /* Front side */
  .brand {
    position: absolute; inset: 0;
    display: flex; align-items: center; justify-content: center;
  }
  .brand__name {
    font-family: "Oswald", "Arial Narrow", sans-serif; font-weight: 400;
    font-size: 50px; letter-spacing: 2px; line-height: 1;
  }
</style>
</head>
<body>
<main class="stage">
  <section class="card card--back" aria-label="Card back">
    <div class="contact">
      <div class="person">
        <p class="person__name">MARA ELLISON</p>
        <p class="person__role">President</p>
        <p>4120 Willow Crest Road</p>
        <p>Halden, Canada 58213</p>
      </div>
      <div class="divider"></div>
      <ul class="details">
        <li>
          <svg viewBox="0 0 12 12" aria-hidden="true"><path d="M2.5 1 L4.5 1 L5 3.5 L3.8 4.5 Q5 7 7.5 8.2 L8.5 7 L11 7.5 L11 9.5 Q10 11 8 10.8 Q2 9.5 1.2 3.5 Q1 1.8 2.5 1 Z" fill="var(--accent)"/></svg>
          512-804-1937
        </li>
        <li>
          <svg viewBox="0 0 12 12" aria-hidden="true"><rect x="3" y="0.8" width="6" height="10.4" rx="1" fill="none" stroke="var(--accent)" stroke-width="1.3"/><circle cx="6" cy="9.3" r=".7" fill="var(--accent)"/></svg>
          512-806-2275
        </li>
        <li>
          <svg viewBox="0 0 12 12" aria-hidden="true"><rect x="0.8" y="2.5" width="10.4" height="7" fill="none" stroke="var(--accent)" stroke-width="1.2"/><path d="M0.8 2.5 L6 6.5 L11.2 2.5" fill="none" stroke="var(--accent)" stroke-width="1.2"/></svg>
          info@kevapilates.co
        </li>
        <li>
          <svg viewBox="0 0 12 12" aria-hidden="true"><circle cx="6" cy="6" r="5" fill="none" stroke="var(--accent)" stroke-width="1.2"/><ellipse cx="6" cy="6" rx="2.2" ry="5" fill="none" stroke="var(--accent)" stroke-width="1"/><path d="M1 6 H11" stroke="var(--accent)" stroke-width="1"/></svg>
          www.kevapilates.com
        </li>
      </ul>
    </div>
    <p class="slogan">No ordinary place</p>
  </section>

  <section class="card card--front" aria-label="Card front">
    <div class="brand">
      <p class="brand__name">Keva Pilates</p>
    </div>
  </section>
</main>
</body>
</html>
```